Corvane Electrical Solutions

On one side. LOGO (underneath:) Commercial Industrial Residential

- NAME & CONTACT DETAILS

Marcus T. Hollings
Project Manager

(Cell icon) (441) 582-6197
(Email icon) cvnelectricalsoultions@mailventra.com
(Facebook & Instagram icons )@cvnelectricalsolutions

Other side: LOGO - underneath ELECTRICAL CONSTRUCTION & MAINTENANCE . LED LIGHTING & AUTOMATION . LIFE SAFETY SYSTEMS (FIRE ALARM / SECURITY) . DATA & COMMUNICATION

```html
<!DOCTYPE html>
<html lang="en">
<head>
<meta charset="utf-8">
<title>Corvane Electrical Solutions – Business Card</title>
<link rel="stylesheet" href="https://fonts.googleapis.com/css2?family=Source+Sans+3:wght@400;600;700&family=Roboto+Condensed:wght@700&display=swap">
<style>
  :root {
    --teal: #13566b;
    --ink: #333333;
    --divider: #4a4a4a;
    --paper: #ffffff;
    --backdrop: #e6e6e6;
    --map-tone: #f1f1f1;
  }
  * { margin: 0; padding: 0; box-sizing: border-box; }
  html, body { width: 1200px; height: 1200px; overflow: hidden; }
  body {
    background: var(--backdrop);
    font-family: "Source Sans 3", "Helvetica Neue", Arial, sans-serif;
    position: relative;
  }
  .card {
    position: absolute;
    left: 205px;
    width: 790px;
    height: 475px;
    background: var(--paper);
    overflow: hidden;
    box-shadow: 0 4px 14px rgba(0,0,0,0.12);
  }
  .card--front { top: 100px; }
  .card--back { top: 655px; }

  /* Front */
  .contact-panel {
    position: absolute; left: 0; top: 0; width: 395px; height: 100%;
    background: var(--teal); color: var(--paper);
  }
  .panel-divider {
    position: absolute; left: 391px; top: 95px; width: 8px; height: 287px;
    background: var(--divider);
  }
  .person-name {
    position: absolute; left: 35px; top: 90px;
    font-size: 31px; font-weight: 400; letter-spacing: -0.3px; line-height: 1;
  }
  .person-name strong { font-weight: 700; }
  .person-title {
    position: absolute; left: 35px; top: 124px;
    font-size: 22px; font-weight: 400; line-height: 1;
  }
  .title-rule {
    position: absolute; left: 35px; top: 153px; width: 50px; height: 3px;
    background: var(--paper);
  }
  .contact-row {
    position: absolute; left: 35px; display: flex; align-items: center; gap: 10px;
    font-size: 18.5px; line-height: 1; letter-spacing: -0.3px; white-space: nowrap;
  }
  .contact-row--phone { top: 249px; }
  .contact-row--email { top: 288px; }
  .contact-icon {
    width: 26px; height: 26px; border-radius: 50%; background: var(--paper);
    display: flex; align-items: center; justify-content: center; flex: none;
  }
  .social-group { position: absolute; left: 35px; top: 327px; }
  .social-dot {
    position: absolute; left: 0; width: 26px; height: 26px; border-radius: 50%;
    background: var(--paper);
  }
  .social-dot--first { top: 0; }
  .social-dot--second { top: 31px; }
  .social-brace {
    position: absolute; left: 31px; top: 4px; font-size: 40px; font-weight: 400; line-height: 1;
  }
  .social-handle {
    position: absolute; left: 49px; top: 19px; font-size: 18.5px; line-height: 1;
    letter-spacing: -0.3px; white-space: nowrap;
  }

  .brand-block {
    position: absolute; left: 400px; top: 0; width: 390px; height: 100%;
    display: flex; flex-direction: column; align-items: center; justify-content: center;
  }
  .brand-name {
    color: var(--teal); font-weight: 600; text-align: center; line-height: 1.05;
  }
  .brand-block .brand-name { font-size: 34px; margin-top: -28px; }
  .brand-tagline {
    margin-top: 20px;
    font-family: "Roboto Condensed", "Arial Narrow", sans-serif;
    font-weight: 700; font-size: 16px; color: var(--ink); letter-spacing: 0.1px;
  }

  /* Back */
  .world-map {
    position: absolute; left: 102px; top: 34px; width: 590px; height: 334px;
    background: radial-gradient(ellipse at center, #ececec 0%, var(--map-tone) 55%, var(--paper) 100%);
  }
  .back-brand {
    position: absolute; left: 0; top: 0; width: 100%; height: 380px;
    display: flex; align-items: center; justify-content: center;
  }
  .back-brand .brand-name { font-size: 46px; margin-top: 8px; }
  .services-band {
    position: absolute; left: 0; bottom: 0; width: 100%; height: 95px;
    background: var(--teal); color: var(--paper);
    display: flex; flex-direction: column; align-items: center; justify-content: center;
    font-size: 22px; line-height: 1.3; letter-spacing: 0.3px;
  }
</style>
</head>
<body>

<section class="card card--front">
  <div class="contact-panel">
    <h1 class="person-name"><strong>Marcus</strong> T. Hollings</h1>
    <p class="person-title">Project Manager</p>
    <div class="title-rule"></div>

    <div class="contact-row contact-row--phone">
      <span class="contact-icon">
        <svg width="12" height="17" viewBox="0 0 12 17" aria-hidden="true">
          <rect x="1" y="1" width="10" height="15" rx="2" fill="none" stroke="#13566b" stroke-width="1.6"/>
          <line x1="4.5" y1="13" x2="7.5" y2="13" stroke="#13566b" stroke-width="1.4"/>
        </svg>
      </span>
      <span>(441) 582-6197</span>
    </div>

    <div class="contact-row contact-row--email">
      <span class="contact-icon">
        <svg width="16" height="12" viewBox="0 0 16 12" aria-hidden="true">
          <rect x="1" y="1" width="14" height="10" rx="1" fill="none" stroke="#13566b" stroke-width="1.3"/>
          <polyline points="1.5,1.8 8,7 14.5,1.8" fill="none" stroke="#13566b" stroke-width="1.3"/>
        </svg>
      </span>
      <span>cvnelectricalsoultions@mailventra.com</span>
    </div>

    <div class="social-group">
      <span class="social-dot social-dot--first"></span>
      <span class="social-dot social-dot--second"></span>
      <span class="social-brace">}</span>
      <span class="social-handle">@cvnelectricalsolutions</span>
    </div>
  </div>
  <div class="panel-divider"></div>

  <div class="brand-block">
    <p class="brand-name">Corvane<br>Electrical Solutions</p>
    <p class="brand-tagline">COMMERCIAL INDUSTRIAL RESIDENTIAL</p>
  </div>
</section>

<section class="card card--back">
  <div class="world-map" role="img" aria-label="Faint dotted world map in light grey"></div>
  <div class="back-brand">
    <p class="brand-name">Corvane<br>Electrical Solutions</p>
  </div>
  <div class="services-band">
    <p>Electrical Construction &amp; Maintenance | Led Lighting &amp; Automation</p>
    <p>Life Safety Systems (fire Alarm / Security) | Data &amp; Communication</p>
  </div>
</section>

</body>
</html>
```